Criação de Papelaria Profissional para Logística, Entrega & Armazenamento
A empresa queria:
" Somos a evolução do Self Storage. Buscamos , armazenamos, levamos de volta , tendo tudo que está armazenado com fotos no sistema, sendo tudo feito pela internet. "

```html
<!DOCTYPE html>
<html lang="pt-BR">
<head>
<meta charset="UTF-8">
<title>Guardaki – Cartão de Visita</title>
<link rel="stylesheet" href="https://fonts.googleapis.com/css2?family=Montserrat:wght@800&family=Roboto+Condensed:wght@400;500&display=swap">
<style>
  :root {
    --backdrop: #e8e5e1;
    --card-white: #ffffff;
    --brand-blue: #3ca8e0;
    --ink-black: #141414;
    --text-dark: #111418;
  }
  * { margin: 0; padding: 0; box-sizing: border-box; }
  html, body { width: 1200px; height: 1200px; overflow: hidden; }
  body {
    background: var(--backdrop);
    position: relative;
    font-family: "Roboto Condensed", Arial, sans-serif;
  }
  .business-card {
    position: absolute;
    left: 50px;
    top: 465px;
    width: 1100px;
    height: 270px;
    border-radius: 24px;
    overflow: hidden;
    background: var(--card-white);
    box-shadow: 0 6px 18px rgba(0,0,0,0.18);
  }
  .card-shapes { position: absolute; inset: 0; width: 100%; height: 100%; }
  .brand-name {
    position: absolute;
    left: 60px;
    top: 0;
    height: 270px;
    display: flex;
    align-items: center;
    gap: 18px;
    font-family: "Montserrat", Arial, sans-serif;
    font-weight: 800;
    font-size: 62px;
    letter-spacing: -1px;
    color: var(--ink-black);
  }
  .brand-mark {
    width: 44px;
    height: 44px;
    background: var(--brand-blue);
    border-radius: 6px;
  }
  .contact-block {
    position: absolute;
    left: 565px;
    top: 24px;
    color: var(--text-dark);
  }
  .person-name {
    font-size: 36px;
    font-weight: 400;
    line-height: 1;
    letter-spacing: 0.5px;
  }
  .person-role {
    font-size: 17px;
    font-weight: 500;
    margin-top: 8px;
    letter-spacing: 0.5px;
  }
  .contact-list { list-style: none; margin-top: 18px; }
  .contact-item {
    display: flex;
    align-items: center;
    gap: 14px;
    font-size: 17px;
    line-height: 1.1;
    margin-bottom: 14px;
    letter-spacing: 0.3px;
  }
  .contact-icon { width: 22px; height: 22px; flex: none; }
  .contact-item strong { font-weight: 500; }
</style>
</head>
<body>
  <div class="business-card">
    <svg class="card-shapes" viewBox="0 0 1100 270" preserveAspectRatio="none" aria-hidden="true">
      <path d="M505 0 C470 80 470 190 480 270 L470 270 C455 190 455 80 490 0 Z" fill="var(--ink-black)"/>
      <path d="M520 0 L1100 0 L1100 270 L495 270 C485 190 485 80 520 0 Z" fill="var(--brand-blue)"/>
      <path d="M490 0 L520 0 C485 80 485 190 495 270 L480 270 C470 190 470 80 505 0 Z" fill="var(--ink-black)"/>
    </svg>

    <div class="brand-name"><span class="brand-mark"></span>Guardaki</div>

    <div class="contact-block">
      <h1 class="person-name">NOME COMPLETO</h1>
      <p class="person-role">CARGO OU FUNÇÃO</p>
      <ul class="contact-list">
        <li class="contact-item">
          <svg class="contact-icon" viewBox="0 0 24 24"><path d="M6.6 10.8c1.4 2.8 3.8 5.1 6.6 6.6l2.2-2.2c.3-.3.7-.4 1-.2 1.1.4 2.3.6 3.6.6.6 0 1 .4 1 1V20c0 .6-.4 1-1 1C10.6 21 3 13.4 3 4c0-.6.4-1 1-1h3.5c.6 0 1 .4 1 1 0 1.3.2 2.5.6 3.6.1.3 0 .7-.2 1z" fill="var(--ink-black)"/></svg>
          <span>00 0000.00000<br>00 0000.00000</span>
        </li>
        <li class="contact-item">
          <svg class="contact-icon" viewBox="0 0 24 24" fill="none" stroke="var(--ink-black)" stroke-width="2"><circle cx="12" cy="12" r="9"/><path d="M3 12h18M12 3c3 3 3 15 0 18M12 3c-3 3-3 15 0 18"/></svg>
          <span>GUARDAKI.COM.BR<br>CONTATO@GUARDAKI.COM.BR</span>
        </li>
        <li class="contact-item">
          <svg class="contact-icon" viewBox="0 0 24 24"><path d="M12 2a7 7 0 0 0-7 7c0 5 7 13 7 13s7-8 7-13a7 7 0 0 0-7-7zm0 9.5A2.5 2.5 0 1 1 12 6.5a2.5 2.5 0 0 1 0 5z" fill="var(--ink-black)"/></svg>
          <span>NOME DA RUA, 000 - BAIRRO<br><strong>CIDADE</strong> - ESTADO - <strong>CEP</strong> E PAIS</span>
        </li>
      </ul>
    </div>
  </div>
</body>
</html>
```